Create modern and sleek business card for luxury real estate company

We're a "boutique" real estate office looking for a design that gets across a highly modern luxury brand. Blacks and whites are probably the best colors unless we try a silver foil for the logo. I've attached a version of our current logo here. I'd like to swap out the current font on there with Gotham Light Regular.

I'm looking to have one side of the card have the logo with the space for our agents info on the other side.

Target Market(s)

Young professionals in a "luxury" headspace

Industry/Entity Type

Real estate

Contact Information for Business Card

A place for agent name, cell number, website. The slogan "Quietly Redefining Modern Homes".

Font styles to use
Other font styles liked:
• Gotham Regular

Colors

Designer to choose only greyscale colors for use in the design.

Requirements
Must have
• Matte black as the background color. Clean lines and use of contrast. A specific design aspect that will use silver foil.
Nice to have
• Up in the air on integrating a QR code
Should not have
• Any houses or other real estate related design (ex: a clip art house)

```html
<!DOCTYPE html>
<html lang="en">
<head>
<meta charset="UTF-8">
<title>Crestline Realty — Business Card</title>
<link href="https://fonts.googleapis.com/css2?family=Montserrat:wght@300;400;500&display=swap" rel="stylesheet">
<style>
  :root {
    --backdrop: #161616;
    --card: #1c1c1c;
    --card-edge: #262626;
    --silver: #d4d4d4;
    --silver-soft: #a9a9a9;
    --text-muted: #8a8a8a;
  }
  * { margin: 0; padding: 0; box-sizing: border-box; }
  html, body {
    width: 1200px; height: 900px; overflow: hidden;
    background: var(--backdrop);
    font-family: "Montserrat", Arial, sans-serif;
  }
  .canvas {
    width: 1200px; height: 900px;
    display: flex; flex-direction: column; align-items: center; justify-content: center;
    gap: 36px;
  }
  .card {
    position: relative;
    width: 700px; height: 400px;
    background: var(--card);
    border: 1px solid var(--card-edge);
    border-radius: 22px;
  }
  /* Front */
  .card-front {
    display: flex; flex-direction: column; align-items: center; justify-content: center;
  }
  .brand {
    display: flex; align-items: center; gap: 22px;
    color: var(--silver);
  }
  .brand-mark {
    width: 74px; height: 74px; border-radius: 50%;
    border: 3px solid var(--silver);
  }
  .brand-name {
    font-weight: 400; text-transform: uppercase;
    font-size: 44px; line-height: 1.05; letter-spacing: 2px;
  }
  .slogan {
    margin-top: 42px;
    color: var(--silver);
    font-weight: 400; font-size: 17px; letter-spacing: 3px;
    text-transform: uppercase;
  }
  /* Back */
  .card-back .brand { position: absolute; left: 46px; top: 42px; gap: 12px; }
  .card-back .brand-mark { width: 40px; height: 40px; border-width: 2px; }
  .card-back .brand-name { font-size: 21px; letter-spacing: 1px; }
  .agent { position: absolute; left: 46px; top: 150px; }
  .agent-name {
    color: var(--silver); font-weight: 400; font-size: 22px;
    letter-spacing: 1.5px; text-transform: uppercase;
  }
  .agent-title { color: var(--text-muted); font-weight: 300; font-size: 15px; margin-top: 4px; }
  .contact {
    position: absolute; left: 46px; bottom: 44px;
    list-style: none; display: flex; flex-direction: column; gap: 9px;
  }
  .contact li {
    display: flex; align-items: center; gap: 10px;
    color: var(--silver); font-weight: 400; font-size: 17px; letter-spacing: 0.5px;
  }
  .contact svg { width: 14px; height: 14px; flex: none; }
  .feature-ring {
    position: absolute; right: 58px; top: 50%; transform: translateY(-50%);
    width: 300px; height: 300px;
  }
</style>
</head>
<body>
<main class="canvas">
  <section class="card card-front" aria-label="Card front">
    <div class="brand">
      <span class="brand-mark"></span>
      <span class="brand-name">Crestline<br>Realty</span>
    </div>
    <p class="slogan">Quietly Redefining Modern Homes</p>
  </section>

  <section class="card card-back" aria-label="Card back">
    <div class="brand">
      <span class="brand-mark"></span>
      <span class="brand-name">Crestline<br>Realty</span>
    </div>
    <div class="agent">
      <p class="agent-name">Daniel Marsh</p>
      <p class="agent-title">Director</p>
    </div>
    <ul class="contact">
      <li>
        <svg viewBox="0 0 24 24" fill="var(--silver)"><path d="M6.6 10.8a15 15 0 0 0 6.6 6.6l2.2-2.2a1 1 0 0 1 1-.25 11.4 11.4 0 0 0 3.6.57 1 1 0 0 1 1 1V20a1 1 0 0 1-1 1A17 17 0 0 1 3 4a1 1 0 0 1 1-1h3.5a1 1 0 0 1 1 1c0 1.25.2 2.45.57 3.57a1 1 0 0 1-.25 1z"/></svg>
        555.014.2290
      </li>
      <li>
        <svg viewBox="0 0 24 24" fill="none" stroke="var(--silver)" stroke-width="2"><rect x="3" y="5" width="18" height="14" rx="1"/><path d="M3 6l9 7 9-7"/></svg>
        hello@crestlinehomes.com
      </li>
      <li>
        <svg viewBox="0 0 24 24" fill="none" stroke="var(--silver)" stroke-width="2"><circle cx="12" cy="12" r="9"/><path d="M3 12h18M12 3c3 3 3 15 0 18M12 3c-3 3-3 15 0 18"/></svg>
        www.crestlinehomes.com
      </li>
    </ul>
    <svg class="feature-ring" viewBox="0 0 300 300" aria-hidden="true">
      <circle cx="150" cy="150" r="144" fill="none" stroke="var(--silver-soft)" stroke-width="8"/>
    </svg>
  </section>
</main>
</body>
</html>
```